Summit Enrolla needs a 8.5" X 11" flyer to give to college presidents

We need a flyer design for Summit Enrolla that briefly explains what we do and encourages college presidents to give the flyer to their directors of admission. Please be consistent with our brand www.summitenrolla.example. I've attached an example of a cool three dimensional flyer that I like...but I'm open to all ideas.

FRONT: The first on-line and fully automated recruiting tool that allows admissions officers to electronically contact high school seniors and send them invitations to apply that include estimates of merit aid.

BACK: Summit Enrolla brings your college or university students' mobile devices and desktops. Knowing their credentials, admissions offers can send either a single student or groups of students invitations to apply that include offers of merit aid. Your school’s invitation is a recruiting document that appeals to students and parents with a clear price signal, and to students and counselors with customizable links to your college or universities website, rankings, social media and any particular information or commendation.

For information about how Summit Enrolla fits into your enrollment strategy and expands your access to students, families and counselors, please contact us by phone 866.512.2740 or email admin@summitenrolla.example. An on-line presentation of Summit Enrolla takes less than 30 minutes.

Target Market(s)

college presidents and admissions officers

Industry/Entity Type

Education

Requirements
Must have
• front and back designs
Nice to have
• a look of depth or three dimensions

```html
<!DOCTYPE html>
<html lang="en">
<head>
<meta charset="utf-8">
<title>Summit Enrolla Flyer</title>
<link href="https://fonts.googleapis.com/css2?family=Cinzel:wght@400;700&family=Arimo:wght@400&family=Roboto+Condensed:wght@700&family=Open+Sans:wght@600&display=swap" rel="stylesheet">
<style>
:root{
  --red:#e8101c;
  --red-deep:#c40a14;
  --navy:#1d3a5f;
  --navy-deep:#142a47;
  --white:#ffffff;
  --panel:#f1f1f1;
  --ink:#1a1a1a;
  --logo-navy:#1f3556;
  --photo-light:#6fb6e6;
  --photo-dark:#0f3f75;
}
*{margin:0;padding:0;box-sizing:border-box}
html,body{width:912px;height:1200px;overflow:hidden;background:#fff}
.flyer{position:relative;width:912px;height:1200px;overflow:hidden;background:var(--navy)}
.flyer-shapes{position:absolute;inset:0}
.brand-tab{position:absolute;left:293px;top:0;width:326px;height:108px;background:var(--white);border-radius:0 0 30px 30px;display:flex;align-items:center;justify-content:center}
.brand-name{font-family:"Cinzel",serif;font-weight:700;font-size:27px;color:var(--logo-navy);letter-spacing:1px}
.text-line{position:absolute;left:0;width:100%;text-align:center;white-space:nowrap}
.headline{top:482px;font-family:"Cinzel",serif;font-size:60px;color:var(--white);letter-spacing:2px}
.subhead{top:568px;font-family:"Cinzel",serif;font-size:28px;color:var(--ink);letter-spacing:1px}
.audience{top:730px;font-family:"Cinzel",serif;font-size:38px;color:var(--red);letter-spacing:1px}
.audience-detail{top:790px;font-family:"Arimo",sans-serif;font-size:26px;color:var(--white);letter-spacing:.5px}
.invite{top:890px;font-family:"Roboto Condensed",sans-serif;font-weight:700;font-size:42px;color:var(--red)}
.invite-detail{top:945px;font-family:"Cinzel",serif;font-size:33px;color:var(--ink);letter-spacing:1px}
.contact-bar{position:absolute;left:0;top:1136px;width:100%;display:flex;justify-content:center;gap:30px;font-family:"Open Sans",sans-serif;font-weight:600;font-size:20px;color:var(--white)}
.contact-item{display:flex;align-items:center;gap:7px}
.contact-item svg{width:18px;height:18px}
</style>
</head>
<body>
<div class="flyer">
  <svg class="flyer-shapes" width="912" height="1200" viewBox="0 0 912 1200">
    <defs>
      <linearGradient id="photoTone" x1="0" y1="0" x2="1" y2="1">
        <stop offset="0" stop-color="var(--photo-dark)"/>
        <stop offset=".5" stop-color="var(--photo-light)"/>
        <stop offset="1" stop-color="var(--photo-dark)"/>
      </linearGradient>
      <linearGradient id="redBand" x1="0" x2="1">
        <stop offset="0" stop-color="var(--red-deep)"/>
        <stop offset=".15" stop-color="var(--red)"/>
        <stop offset=".85" stop-color="var(--red)"/>
        <stop offset="1" stop-color="var(--red-deep)"/>
      </linearGradient>
      <linearGradient id="navyBand" x1="0" x2="1">
        <stop offset="0" stop-color="var(--navy-deep)"/>
        <stop offset=".5" stop-color="var(--navy)"/>
        <stop offset="1" stop-color="var(--navy-deep)"/>
      </linearGradient>
    </defs>
    <rect width="912" height="1200" fill="url(#navyBand)"/>
    <rect width="912" height="470" fill="url(#photoTone)" role="img" aria-label="Photo of a hand using a laptop with glowing blue data charts floating above the screen"/>
    <path d="M0 420 Q456 490 912 420 L912 700 Q456 630 0 700 Z" fill="url(#redBand)"/>
    <path d="M0 408 Q456 478 912 408" fill="none" stroke="var(--white)" stroke-width="4"/>
    <path d="M0 712 Q456 642 912 712" fill="none" stroke="var(--white)" stroke-width="4"/>
    <rect x="0" y="868" width="912" height="160" fill="#dcdcdc"/>
    <rect x="36" y="868" width="840" height="160" fill="var(--panel)"/>
    <path d="M0 1120 Q456 1055 912 1120 L912 1200 L0 1200 Z" fill="var(--red)"/>
    <path d="M0 1108 Q456 1043 912 1108" fill="none" stroke="var(--white)" stroke-width="4"/>
  </svg>

  <div class="brand-tab"><span class="brand-name">Summit Enrolla</span></div>

  <h1 class="text-line headline">THE FIRST ON-LINE</h1>
  <p class="text-line subhead">AND FULLY AUTOMATED RECRUITING TOOL</p>
  <p class="text-line audience">THAT ALLOWS ADMISSIONS OFFICERS</p>
  <p class="text-line audience-detail">TO ELECTRONICALLY CONTACT HIGH SCHOOL SENIORS</p>
  <p class="text-line invite">This tool send them invitations to apply</p>
  <p class="text-line invite-detail">That include estimates of merit aid</p>

  <div class="contact-bar">
    <span class="contact-item">
      <svg viewBox="0 0 24 24" aria-hidden="true"><path fill="#fff" d="M6.6 10.8a15 15 0 0 0 6.6 6.6l2.2-2.2a1 1 0 0 1 1-.25 11.4 11.4 0 0 0 3.6.57 1 1 0 0 1 1 1V20a1 1 0 0 1-1 1A17 17 0 0 1 3 4a1 1 0 0 1 1-1h3.5a1 1 0 0 1 1 1c0 1.25.2 2.45.57 3.57a1 1 0 0 1-.25 1Z"/></svg>
      866.512.2740
    </span>
    <span class="contact-item">
      <svg viewBox="0 0 24 24" aria-hidden="true"><rect x="2" y="5" width="20" height="14" fill="#fff"/><path d="M2 5l10 8 10-8" fill="none" stroke="var(--red)" stroke-width="2"/></svg>
      admin@summitenrolla.example
    </span>
    <span class="contact-item">
      <svg viewBox="0 0 24 24" aria-hidden="true"><g fill="none" stroke="#fff" stroke-width="2"><circle cx="12" cy="12" r="9"/><ellipse cx="12" cy="12" rx="4" ry="9"/><path d="M3 12h18"/></g></svg>
      www.summitenrolla.example
    </span>
  </div>
</div>
</body>
</html>
```